Postcard Design Spring Trails D to D

Residential Real Estate, we want to implement a mail campaign in an specific geographic area.We want to include Market information on the area and statistics of the real estate market.This piece is going to be deliver via mail service door to door.

Target Market(s)

Home owners that might be interested in selling their houses

Industry/Entity Type

Real Estate

Font styles to use
Sans Serif

Colors
ec1f27
f78f20

Requirements
Must have
• Attractive look
• Include the information that we just sent to you
• Clear graphics and tables
• Must include clear information about our group

```html
<!DOCTYPE html>
<html lang="en">
<head>
<meta charset="utf-8">
<title>Spring Trails Market Report Postcard</title>
<link rel="stylesheet" href="https://fonts.googleapis.com/css2?family=Arimo:ital,wght@0,400;0,700;1,400;1,700&display=swap">
<style>
  :root {
    --red: #bf1f2a;
    --orange: #f7901e;
    --white: #ffffff;
    --grey: #6b6b6b;
    --font: "Arimo", Arial, sans-serif;
  }
  * { margin: 0; padding: 0; box-sizing: border-box; }
  html, body { width: 1200px; height: 930px; overflow: hidden; background: var(--white); }
  body { font-family: var(--font); position: relative; }

  .masthead { position: absolute; left: 0; top: 0; width: 1200px; height: 162px; background: var(--orange); padding: 26px 0 0 50px; }
  .masthead__place { font-size: 45px; font-weight: 700; font-style: italic; color: var(--red); line-height: 1; }
  .masthead__title { font-size: 37px; font-style: italic; color: var(--white); line-height: 1.05; margin-top: 10px; }
  .masthead__date { font-size: 24px; font-style: italic; color: var(--white); margin-top: 6px; }

  .report { position: absolute; left: 0; top: 175px; width: 1200px; height: 511px; background: var(--red); }

  .letter { position: absolute; left: 50px; top: 12px; width: 606px; color: var(--white); font-style: italic; }
  .letter__greeting { font-size: 27px; font-weight: 700; margin-bottom: 14px; }
  .letter p { font-size: 24.5px; line-height: 30px; text-align: justify; margin-bottom: 18px; }

  .facts { position: absolute; left: 698px; top: 26px; width: 471px; background: var(--white); border-collapse: collapse; }
  .facts caption { background: var(--white); color: var(--red); font-size: 26px; height: 71px; line-height: 71px; text-align: center; }
  .facts td { border: 2px solid var(--white); background: var(--red); color: var(--white); font-size: 24px; height: 39px; padding: 0 6px; }
  .facts td.facts__value { width: 148px; text-align: center; }

  .invite { position: absolute; left: 698px; top: 282px; width: 471px; height: 209px; background: var(--orange); padding: 44px 24px 0; color: var(--white); font-size: 28px; font-weight: 700; font-style: italic; line-height: 30px; text-align: justify; text-align-last: center; }

  .footer { position: absolute; left: 0; top: 700px; width: 1200px; height: 230px; }
  .footer__edge { position: absolute; left: 0; top: 0; width: 61px; height: 230px; background: var(--orange); }
  .footer__brands { position: absolute; left: 61px; top: 0; width: 399px; height: 230px; background: var(--white); }
  .footer__agent { position: absolute; left: 460px; top: 0; width: 740px; height: 230px; background: var(--red); color: var(--white); }
  .footer__rule { position: absolute; left: 0; top: 79px; width: 1200px; height: 5px; background: var(--orange); }

  .brand-group { position: absolute; left: 20px; top: 18px; font-size: 40px; color: var(--grey); letter-spacing: -1px; }
  .brand-office { position: absolute; left: 20px; top: 128px; display: flex; align-items: center; gap: 10px; font-size: 24px; font-weight: 700; color: var(--red); }
  .brand-office__mark { width: 22px; height: 22px; background: var(--red); }

  .agent-name { position: absolute; right: 37px; top: 10px; font-size: 29px; font-weight: 700; font-style: italic; }
  .agent-role { position: absolute; right: 37px; top: 46px; font-size: 23px; }
  .agent-address { position: absolute; left: 22px; top: 108px; font-size: 22.5px; line-height: 29px; }
  .agent-contact { position: absolute; right: 33px; top: 108px; font-size: 22.5px; line-height: 29px; text-align: right; }
</style>
</head>
<body>
  <header class="masthead">
    <div class="masthead__place">Spring Trails</div>
    <div class="masthead__title">Market Report of single family sold and active homes</div>
    <div class="masthead__date">October Results 2015</div>
  </header>

  <main class="report">
    <section class="letter">
      <h2 class="letter__greeting">Dear Spring Trails Neighbor:</h2>
      <p>We expect that this information will be useful for you to learn about the Real estate market in your neighborhood.</p>
      <p>There are 28 properties “Active for Sale” on the market, with an average price of $303,589 USD and $101.06 USD per sf. Average time on market for sale 63 days.</p>
      <p>In process, “Pending to Close” are 9 houses at average price of $252,808 USD with a sale price of $103.11 per sqf. with 34 Days on market.</p>
      <p>The past 6 Months market behavior was as follows: 97 Houses sold at average price of $263,545 with a sale price / sqf. of $100.50.</p>
    </section>

    <table class="facts">
      <caption>Spring Trails 2014 Facts</caption>
      <tr><td>Single Family Properties</td><td class="facts__value">1,677</td></tr>
      <tr><td>Median Square Feet</td><td class="facts__value">2,568</td></tr>
      <tr><td>Median Lot Square Feet</td><td class="facts__value">7,689</td></tr>
      <tr><td>Median Year Built</td><td class="facts__value">2007</td></tr>
    </table>

    <div class="invite">We will be glad to meet with you and have the opportunity to help you with your Real Estate requirements!</div>
  </main>

  <footer class="footer">
    <div class="footer__brands">
      <div class="brand-group">The Marlowe Group</div>
      <div class="brand-office"><span class="brand-office__mark"></span>Harborline Realty</div>
    </div>
    <div class="footer__agent">
      <div class="agent-name">DANIELA MARLOWE</div>
      <div class="agent-role">REALTOR</div>
      <div class="agent-address">2250 Cedar Ridge Parkway Suite 4B<br>Pinecrest, TX 77399<br>www.TheMarloweGroup.com</div>
      <div class="agent-contact">Office: 555-204-1180<br>Mobile: 555-317-6642<br>daniela@danielamarlowe.com</div>
    </div>
    <div class="footer__rule"></div>
    <div class="footer__edge"></div>
  </footer>
</body>
</html>
```